New Business Card Design

We need a business card design for a new company based in Sydney called "Quill and Lantern". This is an online buisness which will have an online store providing imported homewares.
We are looking for something that is different, perhaps even in shape and using the logo that was designed by Tarvello Works.

Attached document is a basic example I want to see more creative versions.

Target Market(s)

Homewares, Interior Design

Industry/Entity Type

Business

Contact Information for Business Card

Company Logo
Company Name
Industry area
Name
Position
Phone
Email
Website
Motto

Requirements
Must have
• Logo
Nice to have
• Social website logos - Chatterloop, Glimmerly, Burblet, Clippadoo, Zorvo+

```html
<!DOCTYPE html>
<html lang="en">
<head>
<meta charset="utf-8">
<title>Quill and Lantern – Business Card</title>
<link href="https://fonts.googleapis.com/css2?family=Open+Sans:wght@400;600&family=Roboto:wght@500;700&family=Dancing+Script:wght@500&display=swap" rel="stylesheet">
<style>
  :root {
    --bg: #e8e5e1;
    --card: #ffffff;
    --ink: #111111;
    --band: #0b0b0b;
    --gold: #c8892a;
    --gold-light: #e9b867;
  }
  html, body {
    margin: 0; padding: 0;
    width: 1200px; height: 1000px;
    overflow: hidden;
    background: var(--bg);
  }
  p { margin: 0; }
  .canvas { position: relative; width: 1200px; height: 1000px; }
  .card {
    position: absolute; left: 265px; width: 665px; height: 397px;
    background: var(--card); border-radius: 24px; overflow: hidden;
    box-shadow: 0 6px 14px rgba(0,0,0,.25);
    font-family: "Open Sans", Arial, sans-serif; color: var(--ink);
  }
  .card--front { top: 73px; }
  .card--back { top: 533px; }

  .band { position: absolute; left: 0; right: 0; background: var(--band); }
  .gold-rule {
    position: absolute; left: 0; right: 0; height: 3px;
    background: linear-gradient(90deg, var(--gold), var(--gold-light), var(--gold));
  }

  .front-band { top: 0; height: 147px; }
  .front-rule { top: 154px; }
  .brand-name {
    position: absolute; font-family: "Open Sans", Arial, sans-serif;
    font-weight: 600; color: #ffffff; white-space: nowrap; line-height: 1.3;
  }
  .front-brand { left: 42px; top: 52px; font-size: 30px; }
  .brand-dot {
    position: absolute; width: 12px; height: 12px; border-radius: 50%;
    background: var(--gold);
  }
  .front-dot { left: 22px; top: 70px; }

  .person { position: absolute; left: 357px; top: 76px; color: #fff; }
  .person__name { font-family: "Roboto", Arial, sans-serif; font-weight: 700; font-size: 19px; line-height: 25px; letter-spacing: .3px; }
  .person__role { font-size: 16px; line-height: 22px; color: #d0d0d0; margin-top: 2px; }

  .contacts { position: absolute; left: 357px; top: 187px; margin: 0; padding: 0; list-style: none; font-size: 16px; }
  .contacts li { display: flex; align-items: center; height: 27px; }
  .contacts svg { width: 14px; height: 14px; margin-right: 8px; fill: var(--ink); }

  .company-line { position: absolute; left: 0; width: 350px; top: 274px; text-align: center; font-size: 16px; line-height: 22px; }
  .social { position: absolute; left: 0; width: 350px; top: 347px; text-align: center; font-size: 10px; line-height: 16px; font-weight: 600; letter-spacing: .2px; }
  .social span + span::before { content: "·"; margin: 0 4px; color: #777; }

  .motto { position: absolute; left: 356px; top: 338px; font-family: "Dancing Script", cursive; font-size: 25px; line-height: 34px; font-weight: 500; white-space: nowrap; }

  .back-tagline { position: absolute; left: 0; right: 0; top: 27px; text-align: center; font-size: 23px; line-height: 31px; }
  .back-rule-top { top: 118px; }
  .back-band { top: 128px; height: 141px; }
  .back-rule-bottom { top: 277px; }
  .back-brand { left: 0; right: 0; top: 172px; text-align: center; font-size: 40px; }
  .back-web { position: absolute; left: 0; right: 0; top: 345px; text-align: center; font-size: 17px; line-height: 24px; letter-spacing: .5px; }
</style>
</head>
<body>
<main class="canvas">
  <section class="card card--front" aria-label="Business card front">
    <div class="band front-band"></div>
    <div class="gold-rule front-rule"></div>
    <span class="brand-dot front-dot"></span>
    <span class="brand-name front-brand">Quill and Lantern</span>

    <div class="person">
      <p class="person__name">MARISOL VEGA DUNN</p>
      <p class="person__role">Director / Designer</p>
    </div>

    <ul class="contacts">
      <li><svg viewBox="0 0 16 16" aria-hidden="true"><path d="M3 2h3l1 3-2 1a9 9 0 0 0 5 5l1-2 3 1v3a1 1 0 0 1-1 1A13 13 0 0 1 2 3a1 1 0 0 1 1-1z"/></svg>+61 400 555 017</li>
      <li><svg viewBox="0 0 16 16" aria-hidden="true"><path d="M1 3h14v10H1z M1 3l7 6 7-6" fill="none" stroke="#111" stroke-width="1.6"/></svg>marisol@quillandlantern.com.au</li>
      <li><svg viewBox="0 0 16 16" aria-hidden="true"><circle cx="8" cy="8" r="6.5" fill="none" stroke="#111" stroke-width="1.6"/><path d="M1.5 8h13M8 1.5c-3 3-3 10 0 13M8 1.5c3 3 3 10 0 13" fill="none" stroke="#111" stroke-width="1.2"/></svg>www.quillandlantern.com.au</li>
    </ul>

    <p class="company-line">Quill and Lantern<br>European &amp; Imported Homewares</p>
    <p class="social" aria-label="Social channels">
      <span>Chatterloop</span><span>Glimmerly</span><span>Burblet</span><span>Clippadoo</span><span>Zorvo+</span>
    </p>
    <p class="motto">Adding Style to your Home</p>
  </section>

  <section class="card card--back" aria-label="Business card back">
    <p class="back-tagline">Imported Homewares</p>
    <div class="gold-rule back-rule-top"></div>
    <div class="band back-band"></div>
    <div class="gold-rule back-rule-bottom"></div>
    <span class="brand-name back-brand">Quill and Lantern</span>
    <p class="back-web">www.quillandlantern.com.au</p>
  </section>
</main>
</body>
</html>
```